Refresh of Business Card Design

Want to refresh the business card design with the new logo while adhering to style guide as attached. Would like to match feel of website www.quorbeldrives.com

```html
<!DOCTYPE html>
<html lang="en">
<head>
<meta charset="utf-8">
<title>Quorbel Drives — Business Card</title>
<link rel="stylesheet" href="https://fonts.googleapis.com/css2?family=Work+Sans:wght@400;500;700&display=swap">
<style>
  :root {
    --stage: #9a9a9a;
    --card: #000000;
    --accent: #e8173a;
    --ink-light: #ffffff;
    --ink-soft: #d4d4d4;
    --ink-muted: #7a7a7a;
    --ghost: #0c0c0c;
    --ghost-line: #161616;
  }
  * { margin: 0; padding: 0; box-sizing: border-box; }
  html, body {
    width: 1200px; height: 1200px; overflow: hidden;
    background: var(--stage);
    font-family: "Work Sans", sans-serif;
  }
  .canvas { position: relative; width: 1200px; height: 1200px; }
  .card {
    position: absolute; left: 228px; width: 745px; height: 435px;
    background: var(--card); border-radius: 22px; overflow: hidden;
  }
  .card--front { top: 146px; }
  .card--back { top: 618px; }

  .ghost-mark {
    position: absolute; left: 4px; top: 16px; width: 400px; height: 400px;
    border-radius: 50%; background: var(--ghost);
    border: 3px solid var(--ghost-line);
  }

  .holder { position: absolute; left: 406px; top: 106px; }
  .holder__name {
    font-weight: 700; font-size: 27px; letter-spacing: 0.3px;
    color: var(--accent); line-height: 1;
  }
  .holder__role {
    margin-top: 10px; font-weight: 700; font-size: 20px;
    color: var(--ink-light); line-height: 1;
  }

  .contacts { position: absolute; left: 406px; top: 194px; list-style: none; }
  .contacts__item {
    display: flex; align-items: center; height: 23.5px;
    font-size: 19px; color: var(--ink-soft);
  }
  .contacts__icon { width: 12px; height: 12px; margin-right: 11px; fill: var(--accent); }

  .address {
    position: absolute; left: 406px; top: 300px;
    font-style: normal; font-size: 19px; font-weight: 500;
    line-height: 24px; color: var(--ink-muted);
  }

  .brand {
    position: absolute; left: 50%; top: 50%; transform: translate(-50%, -50%);
    display: flex; align-items: center; gap: 14px; white-space: nowrap;
  }
  .brand__dot { width: 30px; height: 30px; border-radius: 50%; background: var(--accent); }
  .brand__name {
    font-weight: 700; font-size: 30px; letter-spacing: 1px; color: var(--ink-light);
  }
</style>
</head>
<body>
<main class="canvas">
  <section class="card card--front" aria-label="Card front">
    <div class="ghost-mark" aria-hidden="true"></div>

    <div class="holder">
      <h1 class="holder__name">DANA WHITLOCK</h1>
      <p class="holder__role">SALES</p>
    </div>

    <ul class="contacts">
      <li class="contacts__item">
        <svg class="contacts__icon" viewBox="0 0 24 24" aria-hidden="true"><path d="M6.6 10.8a15.2 15.2 0 0 0 6.6 6.6l2.2-2.2a1 1 0 0 1 1-.25 11.4 11.4 0 0 0 3.6.57 1 1 0 0 1 1 1V20a1 1 0 0 1-1 1A17 17 0 0 1 3 4a1 1 0 0 1 1-1h3.5a1 1 0 0 1 1 1c0 1.25.2 2.45.57 3.57a1 1 0 0 1-.25 1z"/></svg>
        806.555.0142
      </li>
      <li class="contacts__item">
        <svg class="contacts__icon" viewBox="0 0 24 24" aria-hidden="true"><path d="M2 5h20v14H2z M2 5l10 8 10-8" stroke="#000" stroke-width="1.6"/></svg>
        dwhitlock@quorbeldrives.com
      </li>
      <li class="contacts__item">
        <svg class="contacts__icon" viewBox="0 0 24 24" aria-hidden="true"><circle cx="12" cy="12" r="10"/><path d="M2 12h20M12 2c3 3 3 17 0 20M12 2c-3 3-3 17 0 20" stroke="#000" stroke-width="1.6" fill="none"/></svg>
        quorbeldrives.com
      </li>
    </ul>

    <address class="address">PO Box 40219 Marlow<br>Texas 79705</address>
  </section>

  <section class="card card--back" aria-label="Card back">
    <div class="brand">
      <span class="brand__dot" aria-hidden="true"></span>
      <span class="brand__name">QUORBEL DRIVES</span>
    </div>
  </section>
</main>
</body>
</html>
```